Cedar Row Maintenance and Concierge Flyer

We need a flyer for cedar row maintenance and concierge service. We specialize in and provide residential maintenance and errand services to retired and semi retired persons living in the Lake Norman area. The services we include:
Lighting and plumbing repairs
Ceiling fan installation
Handicap accessories
Locks and security
Picture hanging
Hang blinds
Furniture arrangement / assembly
Pressure washing
Battery Jump start
and more...

Our Concierge services include:
Errand running
Grocery shopping
Wellness Checks
Dog Walk
Garbage Collection
and more...

We offer monthly service agreements and 24/7 access
Call text or e-mail for more information
704.555.0187
1cedarrowmaint@quillpostmail.com

The design should invoke a sense of trust and a customer service driven mission

Target Market(s)

Residential maintenance

Industry/Entity Type

Property Maintenance

Contact Information for Business Card

Derek Halvorsen
48176 Quimby Ferrel Rd.
Cornelius NC 28031
704.555.0187
with uploaded logo

Requirements
Nice to have
• Would like a postcard size flyer. Front and back
Should not have
• No pics of of people wearing hard hats or pics of blueprints. No pics of commercial or industrial maintenance.

```html
<!DOCTYPE html>
<html lang="en">
<head>
<meta charset="utf-8">
<title>Cedar Row Maintenance and Concierge Flyer</title>
<link rel="stylesheet" href="https://fonts.googleapis.com/css2?family=Archivo+Black&family=Open+Sans:wght@400;600&family=Roboto+Condensed:wght@400;700&display=swap">
<style>
  :root {
    --red: #d21f26;
    --red-deep: #9e1419;
    --ink: #111111;
    --ink-soft: #2a2a2a;
    --grey-line: #b9bcc0;
    --paper: #ffffff;
    --paper-shade: #eeeeee;
    --photo-light: #dfe3e8;
    --photo-dark: #7d858e;
  }
  * { margin: 0; padding: 0; box-sizing: border-box; }
  html, body { width: 1200px; height: 907px; overflow: hidden; background: var(--paper); }
  .flyer {
    position: relative;
    width: 1200px; height: 907px;
    background: linear-gradient(180deg, var(--paper) 0%, var(--paper-shade) 100%);
    font-family: "Open Sans", sans-serif;
    color: var(--ink-soft);
    overflow: hidden;
  }
  .shapes { position: absolute; inset: 0; }

  .brand {
    position: absolute; left: 36px; top: 66px;
    display: flex; align-items: center; gap: 16px;
  }
  .brand-dot { width: 54px; height: 54px; border-radius: 50%; background: var(--red); flex: none; }
  .brand-name {
    font-family: "Roboto Condensed", sans-serif; font-weight: 400;
    font-size: 31px; line-height: 1.1; color: var(--ink-soft); width: 400px;
  }

  .headline {
    position: absolute; left: 532px; top: 46px;
    font-family: "Roboto Condensed", sans-serif; font-weight: 700;
    font-size: 86px; line-height: 1; color: var(--red); letter-spacing: -0.5px;
  }
  .subline {
    position: absolute; left: 536px; top: 144px;
    font-family: "Roboto Condensed", sans-serif; font-weight: 700;
    font-size: 25px; color: var(--ink);
  }

  .services-tab {
    position: absolute; left: 0; top: 214px;
    width: 290px; height: 48px;
    background: var(--ink); border-radius: 0 24px 24px 0;
    font-family: "Roboto Condensed", sans-serif; font-weight: 700;
    font-size: 34px; line-height: 48px; color: var(--paper); padding-left: 56px;
  }
  .services { position: absolute; top: 294px; list-style: none; }
  .services.col-a { left: 60px; width: 300px; }
  .services.col-b { left: 380px; width: 290px; }
  .services li {
    position: relative; padding-left: 28px; margin-bottom: 16px;
    font-size: 21px; line-height: 28px; color: var(--ink-soft);
  }
  .services li::before {
    content: ""; position: absolute; left: 0; top: 8px;
    width: 12px; height: 12px; border-radius: 50%; background: var(--red);
  }

  .offer {
    position: absolute; left: 0; top: 557px; width: 572px; height: 228px;
    background: linear-gradient(180deg, var(--red) 0%, var(--red-deep) 100%);
    border-top: 12px solid var(--grey-line);
  }
  .offer-title {
    position: absolute; left: 42px; top: 592px;
    font-family: "Archivo Black", sans-serif; font-size: 50px; line-height: 1; color: var(--ink);
    letter-spacing: 1px;
  }
  .offer-line {
    position: absolute; left: 42px; top: 650px;
    font-family: "Roboto Condensed", sans-serif; font-weight: 700;
    font-size: 32px; color: var(--paper);
  }
  .offer-access {
    position: absolute; left: 40px; top: 688px;
    font-family: "Roboto Condensed", sans-serif; font-weight: 700;
    font-size: 80px; line-height: 1; color: var(--paper);
  }

  .contact {
    position: absolute; left: 0; top: 785px; width: 572px; height: 122px;
    background: var(--ink); padding: 20px 0 0 42px; list-style: none;
  }
  .contact li {
    display: flex; align-items: center; gap: 14px;
    font-family: "Roboto Condensed", sans-serif; font-weight: 400;
    font-size: 29px; line-height: 40px; color: var(--paper); letter-spacing: 0.5px;
  }
  .contact svg { width: 26px; height: 26px; flex: none; }
</style>
</head>
<body>
<main class="flyer">
  <svg class="shapes" width="1200" height="907" viewBox="0 0 1200 907">
    <defs>
      <linearGradient id="photoTone" x1="0" y1="0" x2="1" y2="1">
        <stop offset="0" stop-color="var(--photo-light)"/>
        <stop offset="1" stop-color="var(--photo-dark)"/>
      </linearGradient>
    </defs>
    <path role="img" aria-label="Photo area: three smiling women in business attire at a desk, one holding house keys, one a small model house, one a fan of banknotes"
          d="M572 907 Q640 360 1200 262 L1200 907 Z" fill="url(#photoTone)"/>
    <path class="arc-grey" d="M548 907 Q612 330 1200 236" fill="none" stroke="var(--grey-line)" stroke-width="10"/>
    <path class="arc-red" d="M562 907 Q628 346 1200 250" fill="none" stroke="var(--red)" stroke-width="9"/>
  </svg>

  <div class="brand">
    <span class="brand-dot"></span>
    <span class="brand-name">Cedar Row Maintenance &amp; Concierge</span>
  </div>

  <h1 class="headline">We Specialize in</h1>
  <p class="subline">And provide reSidential maintenance and errand services</p>

  <div class="services-tab">Our services</div>
  <ul class="services col-a">
    <li>Hang blinds</li>
    <li>Furniture arrangement assembly</li>
    <li>Pressure washing</li>
    <li>Battery Jump start</li>
    <li>Picture hanging</li>
  </ul>
  <ul class="services col-b">
    <li>Lighting and plumbing repairs</li>
    <li>Ceiling fan installation</li>
    <li>Handicap accessories</li>
    <li>Locks and security and more</li>
  </ul>

  <section class="offer"></section>
  <div class="offer-title">WE OFFER</div>
  <div class="offer-line">monthly service agreements</div>
  <div class="offer-access">and 24/7 access</div>

  <ul class="contact">
    <li>
      <svg viewBox="0 0 24 24" aria-hidden="true"><rect x="1" y="1" width="22" height="22" rx="4" fill="none" stroke="#fff" stroke-width="2"/><path d="M8 5c1 0 2 3 2 4s-1.5 1.2-1 2.4c.8 1.6 2 2.8 3.6 3.6 1.2.5 1.4-1 2.4-1s4 1 4 2-1.5 3-3 3C10 19 5 14 5 8c0-1.5 2-3 3-3z" fill="#fff"/></svg>
      704.555.0187
    </li>
    <li>
      <svg viewBox="0 0 24 24" aria-hidden="true"><rect x="1" y="4" width="22" height="16" fill="#fff"/><path d="M1 4l11 9 11-9" fill="none" stroke="#111" stroke-width="2"/></svg>
      1cedarrowmaint@quillpostmail.com
    </li>
  </ul>
</main>
</body>
</html>
```